Meridale Crest Advisors – Franchise Growth & Development Presentation

Meridale Crest Advisors is an outsourced franchise sales organization (FSO) that helps franchisors grow their franchise systems without the expense and risk of hiring an internal franchise development team.

We are seeking a professional PowerPoint presentation that will be used to present our services to franchisors, franchise executives, founders, and growth-stage franchise brands.

The presentation should communicate the value of partnering with Meridale Crest Advisors, including:

• Fractional franchise sales team versus hiring internal staff
• 30+ years of franchise industry experience
• 550+ franchise sales successes
• Immediate access to established franchise broker relationships
• Proven franchise development processes
• Franchise growth strategy and enterprise value creation
• Potential private equity and exit opportunities through franchise expansion

The presentation should feel like a modern consulting, investment, or growth strategy presentation rather than a typical sales brochure. We want strong visual storytelling, custom infographics, professional diagrams, and clean business-oriented design.

The audience includes business owners, franchise founders, franchise executives, and investors who are evaluating growth strategies for their franchise systems.

Target Market(s)

Primary Audience: Emerging franchisors Growth-stage franchise brands Franchise founders Franchise CEOs Franchise presidents Franchise development executives Secondary Audience: Private equity firms Franchise investors Strategic buyers Franchise consultants

Industry/Entity Type

Franchise Development, Private Equity / Business Expansion

Font styles to use
Other font styles liked:
• Use Montserrat for titles and Open Sans for body text.

Requirements
Must have
• Modern professional business design Consistent branding throughout Custom infographics Comparison graphics Broker network ecosystem graphic Enterprise value graphic Easy-to-read charts and visuals Editable PowerPoint format Professional iconography. www.meridalecrestadvisors.example as reference for colors
Nice to have
• Franchise-related imagery Subtle growth-themed visuals Timeline graphics Data visualization Private equity / valuation style graphics
Should not have
• Cartoon graphics Clip art Overly busy slides Stock-template appearance Bright neon colors Handwritten fonts Excessive text on slides Juvenile or playful design elements

```html
<!DOCTYPE html>
<html lang="en">
<head>
<meta charset="utf-8">
<title>Meridale Crest Advisors – Franchise Growth Presentation</title>
<link href="https://fonts.googleapis.com/css2?family=Montserrat:wght@500;600;700;800&family=Open+Sans:wght@400;600;700&display=swap" rel="stylesheet">
<style>
:root{
  --navy:#112a4b;
  --navy-deep:#0b1f3a;
  --orange:#f7941d;
  --orange-soft:#fde7cc;
  --ink:#1d2330;
  --muted:#5a6270;
  --line:#d9dde3;
  --card:#ffffff;
  --canvas:#e6e6e6;
}
*{box-sizing:border-box;margin:0;padding:0}
html,body{width:1200px;height:2647px;overflow:hidden;background:var(--canvas)}
body{position:relative;font-family:"Open Sans",Arial,sans-serif;color:var(--ink)}
.icon-set{position:absolute;width:0;height:0;overflow:hidden}
.slide{position:absolute;width:502px;height:283px;background:#fff;overflow:hidden;box-shadow:0 1px 3px rgba(0,0,0,.12)}
.col-l{left:80px}.col-r{left:618px}
.h{font-family:"Montserrat",Arial,sans-serif;font-weight:700;color:var(--navy);line-height:1.1}
.o{color:var(--orange)}
.center{text-align:center}
.abs{position:absolute}
.photo{position:absolute}
.footer{position:absolute;left:0;bottom:0;width:502px;height:40px}
.url{position:absolute;left:24px;bottom:3px;font-size:4.5px;color:#fff}
.brand{position:absolute;right:14px;bottom:8px;font-family:"Montserrat",Arial,sans-serif;font-weight:800;font-size:7px;letter-spacing:.4px;color:var(--navy);text-transform:uppercase}
.ic{display:inline-block;width:20px;height:20px;border-radius:50%;border:1.5px solid var(--orange-soft);position:relative;flex:none;background:#fff;color:var(--orange)}
.ic svg{position:absolute;left:20%;top:20%;width:60%;height:60%;fill:currentColor}
.ic.lg{width:42px;height:42px;border:1.5px solid var(--line)}
.ic.lg svg{left:25%;top:25%;width:50%;height:50%}
.ic.md{width:30px;height:30px;border:1.5px solid var(--orange-soft)}
.list{position:absolute;left:24px;list-style:none}
.list li{display:flex;align-items:center;gap:8px;font-size:10px;height:30px}
.card{position:absolute;background:var(--card);border-radius:4px;box-shadow:0 1px 5px rgba(17,42,75,.14);text-align:center;font-family:"Montserrat",Arial,sans-serif;font-weight:700;font-size:8px;color:var(--navy);line-height:1.2}
.card .ic{margin:10px auto 6px;display:block}
.rule{position:absolute;height:1px;background:#9aa3b0}
.sub{position:absolute;font-family:"Montserrat",Arial,sans-serif;font-weight:700;font-size:11px;color:var(--navy);background:#fff;padding:0 8px}
.banner{position:absolute;background:var(--navy);border-radius:4px;color:#fff;display:flex;align-items:center}
.dot{width:18px;height:18px;border-radius:50%;background:var(--orange);margin:0 8px 0 14px;color:#fff;display:flex;align-items:center;justify-content:center}
.dot svg{width:11px;height:11px;fill:currentColor}
.label{position:absolute;font-size:9px;line-height:1.2;color:var(--ink)}
.svc{position:absolute;width:110px;text-align:center;font-size:9.5px;line-height:1.2}
.svc .ic{display:block;margin:0 auto 5px}
.step-note{position:absolute;width:66px;text-align:center;font-size:6.2px;line-height:1.25;color:var(--ink)}
.case{position:absolute;top:50px;width:140px;height:182px;background:#fff;box-shadow:0 1px 5px rgba(17,42,75,.14);border-radius:4px}
.case .tab{position:absolute;left:32px;top:-6px;width:76px;height:12px;border-radius:6px;background:var(--orange);color:var(--navy);font-family:"Montserrat",Arial,sans-serif;font-weight:700;font-size:6px;text-align:center;line-height:12px}
.case .head{height:30px;background:var(--navy);border-radius:4px 4px 0 0;color:#fff;font-family:"Montserrat",Arial,sans-serif;font-weight:700;font-size:8.5px;text-align:center;line-height:32px}
.case p{padding:8px 9px;font-size:6px;line-height:1.35;color:var(--ink)}
table{border-collapse:collapse;font-size:8px}
td,th{padding:0 4px;text-align:left}
th{font-family:"Montserrat",Arial,sans-serif;font-weight:600;font-size:6.5px;color:var(--navy);height:26px;border-bottom:1px solid var(--line)}
td{height:50px;color:var(--ink)}
tr.mid td{border-bottom:1px solid var(--line)}
.pill{position:absolute;height:50px;background:#fff;box-shadow:0 1px 5px rgba(17,42,75,.14);border-radius:4px;display:flex;align-items:center;gap:8px;padding-left:10px;font-size:10px;line-height:1.2}
.eng{position:absolute;font-family:"Montserrat",Arial,sans-serif;font-weight:600;font-size:10px;color:var(--navy);line-height:1.25}
.cost{position:absolute;font-size:8px;line-height:1.1}
.cost div{display:flex;align-items:center;gap:5px}
</style>
</head>
<body>

<svg class="icon-set" aria-hidden="true">
  <symbol id="i-users" viewBox="0 0 24 24"><circle cx="9" cy="8" r="3.2"/><circle cx="16.5" cy="9" r="2.6"/><path d="M3 19c0-3.5 2.7-6 6-6s6 2.5 6 6z"/><path d="M14.5 13.6c3.4-.8 6.5 1.6 6.5 5.4h-4.6c0-2-.6-3.9-1.9-5.4z"/></symbol>
  <symbol id="i-chart" viewBox="0 0 24 24"><rect x="4" y="14" width="3.2" height="7"/><rect x="10" y="11" width="3.2" height="10"/><rect x="16" y="7" width="3.2" height="14"/><path d="M3 11 9 6l4 2 7-5" fill="none" stroke="currentColor" stroke-width="1.8"/></symbol>
  <symbol id="i-gear" viewBox="0 0 24 24"><circle cx="12" cy="12" r="7.5" fill="none" stroke="currentColor" stroke-width="4" stroke-dasharray="2.6 3.2"/><circle cx="12" cy="12" r="5.2" fill="none" stroke="currentColor" stroke-width="2.4"/></symbol>
  <symbol id="i-doc" viewBox="0 0 24 24"><path d="M6 3h9l4 4v14H6z" fill="none" stroke="currentColor" stroke-width="2"/><path d="M9 11h7M9 14h7M9 17h5" stroke="currentColor" stroke-width="1.6"/></symbol>
  <symbol id="i-chat" viewBox="0 0 24 24"><path d="M3 4h18v11H10l-5 4v-4H3z"/></symbol>
  <symbol id="i-target" viewBox="0 0 24 24"><circle cx="12" cy="12" r="9" fill="none" stroke="currentColor" stroke-width="2"/><circle cx="12" cy="12" r="5" fill="none" stroke="currentColor" stroke-width="2"/><circle cx="12" cy="12" r="1.8"/></symbol>
  <symbol id="i-dollar" viewBox="0 0 24 24"><circle cx="12" cy="12" r="9" fill="none" stroke="currentColor" stroke-width="2"/><text x="12" y="16.5" text-anchor="middle" font-size="12" font-weight="700" font-family="Arial,sans-serif">$</text></symbol>
  <symbol id="i-clock" viewBox="0 0 24 24"><circle cx="12" cy="12" r="9" fill="none" stroke="currentColor" stroke-width="2"/><path d="M12 7v5l3.5 2.5" fill="none" stroke="currentColor" stroke-width="2"/></symbol>
  <symbol id="i-check" viewBox="0 0 24 24"><circle cx="12" cy="12" r="9" fill="none" stroke="currentColor" stroke-width="2"/><path d="M7.5 12.5l3 3 6-6.5" fill="none" stroke="currentColor" stroke-width="2.2"/></symbol>
  <symbol id="i-star" viewBox="0 0 24 24"><path d="M12 2.5l2.9 6 6.6.9-4.8 4.6 1.2 6.5L12 17.4 6.1 20.5l1.2-6.5L2.5 9.4l6.6-.9z"/></symbol>
  <symbol id="i-network" viewBox="0 0 24 24"><path d="M12 6 5 18M12 6l7 12M5 18h14" stroke="currentColor" stroke-width="1.6" fill="none"/><circle cx="12" cy="5.5" r="3"/><circle cx="5" cy="18" r="3"/><circle cx="19" cy="18" r="3"/></symbol>
  <symbol id="i-up" viewBox="0 0 24 24"><path d="M3 19 10 12l4 3 7-8" fill="none" stroke="currentColor" stroke-width="2.2"/><path d="M15 6h7v7z"/></symbol>
  <symbol id="i-home" viewBox="0 0 24 24"><path d="M12 3 2 11h3v9h5v-6h4v6h5v-9h3z"/></symbol>
  <symbol id="i-award" viewBox="0 0 24 24"><path d="M8 13 5 22l4-2 3 2 1-6M16 13l3 9-4-2-3 2" /><circle cx="12" cy="9" r="6.5"/></symbol>
  <symbol id="i-bulb" viewBox="0 0 24 24"><path d="M12 2a7 7 0 0 0-4 12.7V17h8v-2.3A7 7 0 0 0 12 2z"/><rect x="8.5" y="18.5" width="7" height="2.2" rx="1"/></symbol>
  <symbol id="i-link" viewBox="0 0 24 24"><rect x="2" y="8" width="12" height="8" rx="4" fill="none" stroke="currentColor" stroke-width="2.2"/><rect x="10" y="8" width="12" height="8" rx="4" fill="none" stroke="currentColor" stroke-width="2.2"/></symbol>
  <symbol id="i-search" viewBox="0 0 24 24"><circle cx="10" cy="10" r="6.5" fill="none" stroke="currentColor" stroke-width="2.4"/><path d="M15 15l6 6" stroke="currentColor" stroke-width="3"/></symbol>
</svg>

<!-- Row 1 -->
<section class="slide col-l" style="top:70px">
  <div class="photo" role="img" aria-label="Photo of two smiling professionals reviewing work at a laptop" style="left:230px;top:0;width:272px;height:240px;background:linear-gradient(120deg,#f4f5f7 0%,#b9bec6 45%,#6f7884 100%)"></div>
  <h1 class="h abs" style="left:24px;top:38px;font-size:21px">Meridale<br>Crest Advisors</h1>
  <p class="h abs o" style="left:24px;top:92px;font-size:14px;font-weight:600">Outsourced Franchise Sales<br>&amp; Growth Experts</p>
  <p class="abs" style="left:24px;top:145px;font-size:9px;line-height:1.25">Helping franchisors grow faster<br>without the cost and risk of building<br>an internal franchise development team.</p>
  <svg class="abs" style="left:0;bottom:0" width="502" height="100" viewBox="0 0 502 100"><path d="M0 60 C150 62 330 40 502 0 L502 100 L0 100Z" fill="var(--navy)"/><path d="M0 64 C160 66 330 50 502 18 L502 100 L0 100Z" fill="#fff"/><path d="M0 70 C140 72 300 64 420 52 C300 74 180 84 0 100Z" fill="var(--orange)"/></svg>
  <div class="brand" style="bottom:26px;font-size:9px">Meridale Crest Advisors</div>
</section>

<section class="slide col-r" style="top:70px">
  <div class="photo" role="img" aria-label="Photo of a business team meeting in a bright office corridor" style="left:308px;top:0;width:194px;height:258px;background:linear-gradient(160deg,#e9ecef 0%,#a4abb5 55%,#4e5866 100%)"></div>
  <h2 class="h abs" style="left:24px;top:20px;font-size:14px">The Challenge Facing<br><span class="o">Emerging Franchisors</span></h2>
  <ul class="list" style="top:63px">
    <li><span class="ic"><svg><use href="#i-users"/></svg></span>Limited franchise sales resources</li>
    <li><span class="ic"><svg><use href="#i-clock"/></svg></span>Founder wearing too many hats</li>
    <li><span class="ic"><svg><use href="#i-chat"/></svg></span>Inconsistent lead follow-up</li>
    <li><span class="ic"><svg><use href="#i-search"/></svg></span>Difficulty recruiting franchisees</li>
    <li><span class="ic"><svg><use href="#i-link"/></svg></span>Lack of broker relationships</li>
    <li><span class="ic"><svg><use href="#i-dollar"/></svg></span>High cost of internal franchise development staff</li>
  </ul>
  <svg class="footer" viewBox="0 0 502 40"><path d="M0 30 C150 28 330 18 502 4 L502 40 L0 40Z" fill="var(--navy)"/><path d="M0 27 C150 25 330 14 502 0 L502 4 C330 18 150 28 0 30Z" fill="var(--orange)"/><path d="M220 40 C330 34 420 24 502 12 L502 40Z" fill="#fff"/></svg>
  <div class="url">2 &nbsp; www.meridalecrestadvisors.example</div>
  <div class="brand">Meridale Crest Advisors</div>
</section>

<!-- Row 2 -->
<section class="slide col-l" style="top:384px">
  <div class="photo" role="img" aria-label="Photo of two colleagues reviewing documents at a desk" style="left:309px;top:0;width:193px;height:258px;background:linear-gradient(150deg,#d8dce1 0%,#8d96a1 55%,#3e4856 100%)"></div>
  <h2 class="h abs" style="left:24px;top:20px;font-size:14px">Why Meridale<br><span class="o">Crest Advisors</span></h2>
  <ul class="list" style="top:63px">
    <li><span class="ic"><svg><use href="#i-users"/></svg></span>Fractional franchise sales team</li>
    <li><span class="ic"><svg><use href="#i-gear"/></svg></span><span><b>30+</b> years franchise industry experience</span></li>
    <li><span class="ic"><svg><use href="#i-chart"/></svg></span><span><b>500+</b> franchise sales successes</span></li>
    <li><span class="ic"><svg><use href="#i-target"/></svg></span>Immediate execution</li>
    <li><span class="ic"><svg><use href="#i-check"/></svg></span>Proven systems and processes</li>
    <li><span class="ic"><svg><use href="#i-network"/></svg></span>Deep broker network relationships</li>
  </ul>
  <svg class="footer" viewBox="0 0 502 40"><path d="M0 30 C150 28 330 18 502 4 L502 40 L0 40Z" fill="var(--navy)"/><path d="M0 27 C150 25 330 14 502 0 L502 4 C330 18 150 28 0 30Z" fill="var(--orange)"/><path d="M220 40 C330 34 420 24 502 12 L502 40Z" fill="#fff"/></svg>
  <div class="url">3 &nbsp; www.meridalecrestadvisors.example</div>
  <div class="brand">Meridale Crest Advisors</div>
</section>

<section class="slide col-r" style="top:384px">
  <div class="photo" role="img" aria-label="Photo of a smiling team of professionals" style="left:0;top:0;width:502px;height:100px;background:linear-gradient(90deg,#3a4150 0%,#6b7280 40%,#2b3240 100%)"></div>
  <h2 class="h abs center" style="left:0;width:502px;top:80px;font-size:14px;color:#fff">The Cost of Hiring vs. Outsourcing</h2>
  <div class="abs center h" style="left:0;top:100px;width:250px;height:28px;background:var(--navy);color:#fff;font-size:9px;padding-top:3px">Internal Franchise<br>Development Director</div>
  <div class="abs center h" style="left:250px;top:100px;width:252px;height:28px;background:var(--orange);color:var(--navy);font-size:9px;padding-top:3px">Meridale<br>Crest Advisors</div>
  <div class="cost" style="left:35px;top:140px">
    <div style="height:27px"><span class="ic"><svg><use href="#i-search"/></svg></span>Recruiting<br>costs</div>
    <div style="height:27px"><span class="ic"><svg><use href="#i-dollar"/></svg></span>Salary</div>
    <div style="height:27px"><span class="ic"><svg><use href="#i-users"/></svg></span>Benefits</div>
    <div style="height:27px"><span class="ic"><svg><use href="#i-doc"/></svg></span>Payroll taxes</div>
  </div>
  <div class="cost" style="left:132px;top:140px">
    <div style="height:33px"><span class="ic"><svg><use href="#i-chat"/></svg></span>Training</div>
    <div style="height:33px"><span class="ic"><svg><use href="#i-clock"/></svg></span>Ramp-up<br>period</div>
    <div style="height:33px"><span class="ic"><svg><use href="#i-target"/></svg></span>Unknown<br>performance</div>
  </div>
  <div class="abs h" style="left:228px;top:186px;font-size:13px">VS</div>
  <div class="abs" style="left:252px;top:142px;width:1px;height:104px;background:var(--line)"></div>
  <div class="cost" style="left:275px;top:140px">
    <div style="height:38px"><span class="ic"><svg><use href="#i-dollar"/></svg></span>Fractional<br>investment</div>
    <div style="height:38px"><span class="ic"><svg><use href="#i-gear"/></svg></span>Entire team<br>of experts</div>
    <div style="height:38px"><span class="ic"><svg><use href="#i-up"/></svg></span>Immediate<br>launch</div>
  </div>
  <div class="cost" style="left:372px;top:140px">
    <div style="height:38px"><span class="ic"><svg><use href="#i-check"/></svg></span>Proven<br>processes</div>
    <div style="height:38px"><span class="ic"><svg><use href="#i-link"/></svg></span>Existing<br>relationships</div>
    <div style="height:38px"><span class="ic"><svg><use href="#i-chart"/></svg></span>Scalable<br>growth</div>
  </div>
  <svg class="footer" viewBox="0 0 502 40"><path d="M0 30 C150 28 330 18 502 4 L502 40 L0 40Z" fill="var(--navy)"/><path d="M0 27 C150 25 330 14 502 0 L502 4 C330 18 150 28 0 30Z" fill="var(--orange)"/><path d="M220 40 C330 34 420 24 502 12 L502 40Z" fill="#fff"/></svg>
  <div class="url">4 &nbsp; www.meridalecrestadvisors.example</div>
  <div class="brand">Meridale Crest Advisors</div>
</section>

<!-- Row 3 -->
<section class="slide col-l" style="top:698px">
  <h2 class="h abs center" style="left:0;width:502px;top:20px;font-size:13.5px">What Takes Years to Build, <span class="o">You Get on Day One</span></h2>
  <svg class="abs" style="left:175px;top:55px" width="140" height="140" viewBox="0 0 140 140">
    <circle cx="70" cy="70" r="52" fill="none" stroke="#f1f2f4" stroke-width="34" stroke-dasharray="43.7 3" transform="rotate(-100 70 70)"/>
    <circle cx="70" cy="70" r="31" fill="#fff" stroke="var(--navy)" stroke-width="1"/>
    <g fill="var(--orange)">
      <use href="#i-link" x="46" y="20" width="14" height="14"/>
      <use href="#i-network" x="82" y="22" width="14" height="14"/>
      <use href="#i-users" x="106" y="50" width="14" height="14"/>
      <use href="#i-doc" x="100" y="87" width="14" height="14"/>
      <use href="#i-up" x="70" y="108" width="14" height="14"/>
      <use href="#i-users" x="32" y="100" width="14" height="14"/>
      <use href="#i-chart" x="19" y="63" width="14" height="14"/>
    </g>
  </svg>
  <p class="label" style="left:100px;top:57px;text-align:right">Franchise broker<br>relationships</p>
  <p class="label" style="left:316px;top:57px">Industry<br>connections</p>
  <p class="label" style="left:84px;top:118px;text-align:right">Franchise sales<br>expertise</p>
  <p class="label" style="left:343px;top:118px">Candidate<br>nurturing systems</p>
  <p class="label" style="left:82px;top:184px;text-align:right">Lead qualification<br>systems</p>
  <p class="label" style="left:331px;top:184px">CRM and reporting<br>infrastructure</p>
  <p class="label center" style="left:0;width:502px;top:233px">Franchise development processes</p>
  <svg class="footer" viewBox="0 0 502 40"><path d="M0 30 C150 28 330 18 502 4 L502 40 L0 40Z" fill="var(--navy)"/><path d="M0 27 C150 25 330 14 502 0 L502 4 C330 18 150 28 0 30Z" fill="var(--orange)"/><path d="M220 40 C330 34 420 24 502 12 L502 40Z" fill="#fff"/></svg>
  <div class="url">5 &nbsp; www.meridalecrestadvisors.example</div>
  <div class="brand">Meridale Crest Advisors</div>
</section>

<section class="slide col-r" style="top:698px">
  <h2 class="h abs center" style="left:0;width:502px;top:16px;font-size:13.5px">Instant Access to<br><span class="o">the Franchise Broker Community</span></h2>
  <div class="rule" style="left:24px;top:70px;width:454px;background:var(--orange)"></div>
  <div class="sub" style="left:182px;top:61px;font-size:8px;font-weight:800;text-transform:uppercase">Meridale Crest Advisors</div>
  <div class="card" style="left:24px;top:84px;width:84px;height:102px"><span class="ic md"><svg><use href="#i-users"/></svg></span>Franchise<br>consultants</div>
  <div class="card" style="left:116px;top:84px;width:84px;height:102px"><span class="ic md"><svg><use href="#i-gear"/></svg></span>Industry<br>partners</div>
  <div class="card" style="left:208px;top:84px;width:84px;height:102px"><span class="ic md"><svg><use href="#i-star"/></svg></span>Franchise<br>influencers</div>
  <div class="card" style="left:300px;top:84px;width:84px;height:102px"><span class="ic md"><svg><use href="#i-link"/></svg></span>Referral<br>sources</div>
  <div class="card" style="left:392px;top:84px;width:84px;height:102px"><span class="ic md"><svg><use href="#i-network"/></svg></span>Broker<br>networks
    <div style="display:grid;grid-template-columns:1fr 1fr;gap:3px;padding:5px 5px 0"><i style="height:7px;border-radius:3px;background:var(--orange-soft)"></i><i style="height:7px;border-radius:3px;background:var(--orange-soft)"></i><i style="height:7px;border-radius:3px;background:var(--orange-soft)"></i><i style="height:7px;border-radius:3px;background:var(--orange-soft)"></i><i style="height:7px;border-radius:3px;background:var(--orange-soft)"></i><i style="height:7px;border-radius:3px;background:var(--orange-soft)"></i></div>
  </div>
  <div class="banner" style="left:24px;top:197px;width:454px;height:34px;justify-content:center;font-size:9.5px">We spent over&nbsp;<b class="o" style="font-size:11px">20 Years</b>&nbsp;building these relationships so your brand doesn't have to.</div>
  <svg class="footer" viewBox="0 0 502 40"><path d="M0 30 C150 28 330 18 502 4 L502 40 L0 40Z" fill="var(--navy)"/><path d="M0 27 C150 25 330 14 502 0 L502 4 C330 18 150 28 0 30Z" fill="var(--orange)"/><path d="M220 40 C330 34 420 24 502 12 L502 40Z" fill="#fff"/></svg>
  <div class="url">6 &nbsp; www.meridalecrestadvisors.example</div>
  <div class="brand">Meridale Crest Advisors</div>
</section>

<!-- Row 4 -->
<section class="slide col-l" style="top:1013px">
  <h2 class="h abs center" style="left:0;width:502px;top:20px;font-size:13.5px">Our Franchise <span class="o">Development Process</span></h2>
  <svg class="abs" style="left:24px;top:117px" width="456" height="42" viewBox="0 -6 456 42" font-family="Montserrat,Arial,sans-serif" font-weight="700" font-size="7" text-anchor="middle">
    <path d="M0 4 H58 L66 18 L58 32 H0Z" fill="var(--navy)"/><text x="31" y="24" fill="#fff">Lead</text>
    <path d="M62 4 H122 L130 18 L122 32 H62 L70 18Z" fill="var(--orange)"/><text x="98" y="24" fill="var(--navy)">Qualification</text>
    <path d="M126 4 H186 L194 18 L186 32 H126 L134 18Z" fill="var(--navy)"/><text x="160" y="24" fill="#fff">Education</text>
    <path d="M190 4 H250 L258 18 L250 32 H190 L198 18Z" fill="var(--orange)"/><text x="224" y="20" fill="var(--navy)">FDD</text><text x="224" y="28" fill="var(--navy)">Review</text>
    <path d="M254 4 H314 L322 18 L314 32 H254 L262 18Z" fill="var(--navy)"/><text x="288" y="24" fill="#fff">Validation</text>
    <path d="M318 4 H378 L386 18 L378 32 H318 L326 18Z" fill="var(--orange)"/><text x="352" y="20" fill="var(--navy)">Discovery</text><text x="352" y="28" fill="var(--navy)">Day</text>
    <path d="M382 4 H446 L454 18 L446 32 H382 L390 18Z" fill="var(--navy)"/><text x="418" y="20" fill="#fff">Franchise</text><text x="418" y="28" fill="#fff">Award</text>
    <g fill="#fff" stroke="var(--orange)" stroke-width="1"><circle cx="31" cy="4" r="7"/><circle cx="98" cy="4" r="7"/><circle cx="160" cy="4" r="7"/><circle cx="224" cy="4" r="7"/><circle cx="288" cy="4" r="7"/><circle cx="352" cy="4" r="7"/><circle cx="418" cy="4" r="7"/></g>
    <g fill="var(--navy)">
      <use href="#i-users" x="26" y="-1" width="10" height="10"/>
      <use href="#i-check" x="93" y="-1" width="10" height="10" fill="var(--orange)" style="color:var(--orange)"/>
      <use href="#i-doc" x="155" y="-1" width="10" height="10" style="color:var(--navy)"/>
      <use href="#i-doc" x="219" y="-1" width="10" height="10" style="color:var(--orange)"/>
      <use href="#i-search" x="283" y="-1" width="10" height="10" style="color:var(--navy)"/>
      <use href="#i-target" x="347" y="-1" width="10" height="10" style="color:var(--orange)"/>
      <use href="#i-award" x="413" y="-1" width="10" height="10"/>
    </g>
  </svg>
  <p class="step-note" style="left:89px;top:76px">We qualify each candidate to ensure alignment with your ideal profile</p>
  <p class="step-note" style="left:215px;top:76px">Candidates review your FDD with our guidance and support.</p>
  <p class="step-note" style="left:343px;top:76px">Candidates visit, meet your team and experience your brand.</p>
  <p class="step-note" style="left:22px;top:166px">We attract and capture potential franchise candidates.</p>
  <p class="step-note" style="left:150px;top:166px">We educate candidates on your brand, business model and opportunity</p>
  <p class="step-note" style="left:278px;top:166px">Candidate validates their fit, capabilities and commitment</p>
  <p class="step-note" style="left:410px;top:166px">The right candidate. The right time. The right Partnership.</p>
  <svg class="footer" viewBox="0 0 502 40"><path d="M0 30 C150 28 330 18 502 4 L502 40 L0 40Z" fill="var(--navy)"/><path d="M0 27 C150 25 330 14 502 0 L502 4 C330 18 150 28 0 30Z" fill="var(--orange)"/><path d="M220 40 C330 34 420 24 502 12 L502 40Z" fill="#fff"/></svg>
  <div class="url">7 &nbsp; www.meridalecrestadvisors.example</div>
  <div class="brand">Meridale Crest Advisors</div>
</section>

<section class="slide col-r" style="top:1013px">
  <h2 class="h abs center" style="left:0;width:502px;top:20px;font-size:13.5px">Services <span class="o">We Provide</span></h2>
  <div class="svc" style="left:24px;top:60px"><span class="ic lg"><svg><use href="#i-doc"/></svg></span>FDD/Operations<br>Review</div>
  <div class="svc" style="left:139px;top:60px"><span class="ic lg"><svg><use href="#i-gear"/></svg></span>Franchise sales<br>outsourcing</div>
  <div class="svc" style="left:253px;top:60px"><span class="ic lg"><svg><use href="#i-users"/></svg></span>Lead<br>qualification</div>
  <div class="svc" style="left:368px;top:60px"><span class="ic lg"><svg><use href="#i-users"/></svg></span>Candidate<br>nurturing</div>
  <div class="svc" style="left:24px;top:152px"><span class="ic lg"><svg><use href="#i-search"/></svg></span>Discovery Day<br>coordination</div>
  <div class="svc" style="left:139px;top:152px"><span class="ic lg"><svg><use href="#i-link"/></svg></span>Broker recruitment<br>/ engagement</div>
  <div class="svc" style="left:253px;top:152px"><span class="ic lg"><svg><use href="#i-network"/></svg></span>CRM<br>management</div>
  <div class="svc" style="left:368px;top:152px"><span class="ic lg"><svg><use href="#i-chart"/></svg></span>Reporting<br>and forecasting</div>
  <svg class="footer" viewBox="0 0 502 40"><path d="M0 30 C150 28 330 18 502 4 L502 40 L0 40Z" fill="var(--navy)"/><path d="M0 27 C150 25 330 14 502 0 L502 4 C330 18 150 28 0 30Z" fill="var(--orange)"/><path d="M220 40 C330 34 420 24 502 12 L502 40Z" fill="#fff"/></svg>
  <div class="url">8 &nbsp; www.meridalecrestadvisors.example</div>
  <div class="brand">Meridale Crest Advisors</div>
</section>

<!-- Row 5 -->
<section class="slide col-l" style="top:1327px">
  <h2 class="h abs center" style="left:0;width:502px;top:18px;font-size:13.5px">Building a Referral Engine<br><span class="o">for Your Brand</span></h2>
  <div class="rule" style="left:24px;top:77px;width:454px"></div>
  <div class="sub" style="left:146px;top:70px">Focus on broker development</div>
  <div class="card" style="left:24px;top:97px;width:108px;height:126px;font-size:8.5px"><span class="ic lg" style="margin:16px auto 12px"><svg><use href="#i-users"/></svg></span>Broker/Consultant<br>education</div>
  <div class="card" style="left:139px;top:97px;width:108px;height:126px;font-size:8.5px"><span class="ic lg" style="margin:16px auto 12px"><svg><use href="#i-chart"/></svg></span>Brand<br>presentations</div>
  <div class="card" style="left:254px;top:97px;width:108px;height:126px;font-size:8.5px"><span class="ic lg" style="margin:16px auto 12px"><svg><use href="#i-chat"/></svg></span>Ongoing<br>communication</div>
  <div class="card" style="left:369px;top:97px;width:108px;height:126px;font-size:8.5px"><span class="ic lg" style="margin:16px auto 12px"><svg><use href="#i-network"/></svg></span>Referral<br>generation</div>
  <svg class="footer" viewBox="0 0 502 40"><path d="M0 30 C150 28 330 18 502 4 L502 40 L0 40Z" fill="var(--navy)"/><path d="M0 27 C150 25 330 14 502 0 L502 4 C330 18 150 28 0 30Z" fill="var(--orange)"/><path d="M220 40 C330 34 420 24 502 12 L502 40Z" fill="#fff"/></svg>
  <div class="url">9 &nbsp; www.meridalecrestadvisors.example</div>
  <div class="brand">Meridale Crest Advisors</div>
</section>

<section class="slide col-r" style="top:1327px">
  <h2 class="h abs center" style="left:0;width:502px;top:20px;font-size:13.5px">Why Experience <span class="o">Matters</span></h2>
  <div class="rule" style="left:24px;top:55px;width:454px"></div>
  <div class="sub" style="left:212px;top:48px">Highlight</div>
  <div class="card" style="left:24px;top:75px;width:146px;height:74px"><span class="ic md"><svg><use href="#i-chart"/></svg></span>500+ franchise sales<br>successes</div>
  <div class="card" style="left:178px;top:75px;width:146px;height:74px"><span class="ic md"><svg><use href="#i-gear"/></svg></span>30+ years industry<br>experience</div>
  <div class="card" style="left:332px;top:75px;width:146px;height:74px"><span class="ic md"><svg><use href="#i-users"/></svg></span>Thousands of franchise<br>candidates evaluated</div>
  <div class="card" style="left:105px;top:156px;width:146px;height:74px"><span class="ic md"><svg><use href="#i-network"/></svg></span>Extensive broker<br>network relationships</div>
  <div class="card" style="left:259px;top:156px;width:146px;height:74px"><span class="ic md"><svg><use href="#i-star"/></svg></span>Multi-brand franchise<br>development expertise</div>
  <svg class="footer" viewBox="0 0 502 40"><path d="M0 30 C150 28 330 18 502 4 L502 40 L0 40Z" fill="var(--navy)"/><path d="M0 27 C150 25 330 14 502 0 L502 4 C330 18 150 28 0 30Z" fill="var(--orange)"/><path d="M220 40 C330 34 420 24 502 12 L502 40Z" fill="#fff"/></svg>
  <div class="url">10 &nbsp; www.meridalecrestadvisors.example</div>
  <div class="brand">Meridale Crest Advisors</div>
</section>

<!-- Row 6 -->
<section class="slide col-l" style="top:1641px">
  <h2 class="h abs center" style="left:0;width:502px;top:20px;font-size:13.5px">Success <span class="o">Stories</span></h2>
  <div class="case" style="left:24px"><div class="tab">Case Study #1</div><div class="head">Heading Text Here</div><p>This placeholder describes how a growing franchise brand partnered with our team to expand its system. We qualified candidates, built broker relationships and guided each prospect through discovery. Within the first year the brand awarded new units across several regions, strengthened royalty revenue and created a repeatable development process that supports long term enterprise value.</p></div>
  <div class="case" style="left:181px"><div class="tab">Case Study #2</div><div class="head">Heading Text Here</div><p>This placeholder describes how a growing franchise brand partnered with our team to expand its system. We qualified candidates, built broker relationships and guided each prospect through discovery. Within the first year the brand awarded new units across several regions, strengthened royalty revenue and created a repeatable development process that supports long term enterprise value.</p></div>
  <div class="case" style="left:338px"><div class="tab">Case Study #3</div><div class="head">Heading Text Here</div><p>This placeholder describes how a growing franchise brand partnered with our team to expand its system. We qualified candidates, built broker relationships and guided each prospect through discovery. Within the first year the brand awarded new units across several regions, strengthened royalty revenue and created a repeatable development process that supports long term enterprise value.</p></div>
  <svg class="footer" viewBox="0 0 502 40"><path d="M0 30 C150 28 330 18 502 4 L502 40 L0 40Z" fill="var(--navy)"/><path d="M0 27 C150 25 330 14 502 0 L502 4 C330 18 150 28 0 30Z" fill="var(--orange)"/><path d="M220 40 C330 34 420 24 502 12 L502 40Z" fill="#fff"/></svg>
  <div class="url">11 &nbsp; www.meridalecrestadvisors.example</div>
  <div class="brand">Meridale Crest Advisors</div>
</section>

<section class="slide col-r" style="top:1641px">
  <h2 class="h abs center" style="left:0;width:502px;top:10px;font-size:13.5px">Building Enterprise Value <span class="o">Through Franchise Growth</span></h2>
  <p class="abs center" style="left:0;width:502px;top:27px;font-size:8px;font-weight:700;color:var(--navy)">Franchise growth creates recurring royalty revenue and increases enterprise value.</p>
  <table class="abs" style="left:24px;top:47px;width:220px">
    <tr><th>Stage</th><th>Units</th><th>Annual Royalty Revenue</th></tr>
    <tr class="mid"><td><b>Early Growth</b></td><td>20</td><td>$165,000</td></tr>
    <tr><td><b>Growth Stage</b></td><td>63</td><td>$1,470,000</td></tr>
  </table>
  <table class="abs" style="left:254px;top:47px;width:222px">
    <tr><th>Royalty Revenue</th><th>10x EBITDA</th><th>15x EBITDA</th></tr>
    <tr class="mid"><td><b>$165,000</b></td><td>$1.65M</td><td>$2.48M</td></tr>
    <tr><td><b>$1,470,000</b></td><td>$14.7M</td><td>$22.05M</td></tr>
  </table>
  <div class="banner" style="left:24px;top:190px;width:454px;height:42px;font-size:7.5px">
    <span class="dot"><svg><use href="#i-bulb"/></svg></span>
    <b class="o" style="font-family:Montserrat,Arial,sans-serif;font-size:7.5px;width:46px;line-height:1.1">Key<br>Takeaway</b>
    <span style="width:1px;height:26px;background:#5b6d86;margin:0 10px"></span>
    <span style="line-height:1.3">Franchise growth is not just about selling franchises.<br>It is about creating recurring royalty revenue that can significantly increase<br>the value of the franchise system.</span>
  </div>
  <svg class="footer" viewBox="0 0 502 40"><path d="M0 30 C150 28 330 18 502 4 L502 40 L0 40Z" fill="var(--navy)"/><path d="M0 27 C150 25 330 14 502 0 L502 4 C330 18 150 28 0 30Z" fill="var(--orange)"/><path d="M220 40 C330 34 420 24 502 12 L502 40Z" fill="#fff"/></svg>
  <div class="url">www.meridalecrestadvisors.example</div>
  <div class="brand">Meridale Crest Advisors</div>
</section>

<!-- Row 7 -->
<section class="slide col-l" style="top:1955px">
  <h2 class="h abs" style="left:24px;top:20px;font-size:13.5px">Creating Future <span class="o">Exit Opportunities</span></h2>
  <div class="rule" style="left:24px;top:52px;width:454px"></div>
  <div class="sub" style="left:178px;top:45px">Potential Outcomes</div>
  <div class="pill" style="left:24px;top:70px;width:144px"><span class="ic md"><svg><use href="#i-users"/></svg></span>Private equity<br>acquisition</div>
  <div class="pill" style="left:178px;top:70px;width:144px"><span class="ic md"><svg><use href="#i-link"/></svg></span>Strategic buyer<br>acquisition</div>
  <div class="pill" style="left:332px;top:70px;width:146px"><span class="ic md"><svg><use href="#i-dollar"/></svg></span>Recapitalization</div>
  <div class="pill" style="left:105px;top:128px;width:144px"><span class="ic md"><svg><use href="#i-home"/></svg></span>Family<br>succession</div>
  <div class="pill" style="left:259px;top:128px;width:144px"><span class="ic md"><svg><use href="#i-dollar"/></svg></span>Long-term cash<br>flow ownership</div>
  <div class="banner" style="left:24px;top:190px;width:454px;height:42px;font-size:8px">
    <span class="dot"><svg><use href="#i-chat"/></svg></span>
    <b class="o" style="font-family:Montserrat,Arial,sans-serif;font-size:8px;width:46px">Message</b>
    <span style="width:1px;height:26px;background:#5b6d86;margin:0 10px"></span>
    Every franchise sold today may contribute to enterprise value tomorrow.
  </div>
  <svg class="footer" viewBox="0 0 502 40"><path d="M0 30 C150 28 330 18 502 4 L502 40 L0 40Z" fill="var(--navy)"/><path d="M0 27 C150 25 330 14 502 0 L502 4 C330 18 150 28 0 30Z" fill="var(--orange)"/><path d="M220 40 C330 34 420 24 502 12 L502 40Z" fill="#fff"/></svg>
  <div class="url">www.meridalecrestadvisors.example</div>
  <div class="brand">Meridale Crest Advisors</div>
</section>

<section class="slide col-r" style="top:1955px">
  <h2 class="h abs center" style="left:0;width:502px;top:20px;font-size:13.5px">Why Meridale Crest <span class="o">Advisors Is Different</span></h2>
  <div class="card" style="left:24px;top:50px;width:108px;height:178px;font-size:9px"><span class="ic lg" style="width:50px;height:50px;margin:36px auto 14px"><svg><use href="#i-chart"/></svg></span><span style="font-size:14px;font-weight:800">550+</span><br>franchise sales</div>
  <div class="card" style="left:139px;top:50px;width:107px;height:86px"><span class="ic md" style="margin-top:16px"><svg><use href="#i-dollar"/></svg></span>Fractional<br>cost model</div>
  <div class="card" style="left:254px;top:50px;width:107px;height:86px"><span class="ic md" style="margin-top:16px"><svg><use href="#i-doc"/></svg></span>Immediate<br>execution</div>
  <div class="card" style="left:369px;top:50px;width:107px;height:86px"><span class="ic md" style="margin-top:16px"><svg><use href="#i-star"/></svg></span>30+ years'<br>experience</div>
  <div class="card" style="left:139px;top:142px;width:107px;height:86px"><span class="ic md" style="margin-top:16px"><svg><use href="#i-network"/></svg></span>Established<br>broker network</div>
  <div class="card" style="left:254px;top:142px;width:107px;height:86px"><span class="ic md" style="margin-top:16px"><svg><use href="#i-gear"/></svg></span>Proven franchise<br>growth systems</div>
  <div class="card" style="left:369px;top:142px;width:107px;height:86px"><span class="ic md" style="margin-top:16px"><svg><use href="#i-up"/></svg></span>Strategic<br>growth partner</div>
  <svg class="footer" viewBox="0 0 502 40"><path d="M0 30 C150 28 330 18 502 4 L502 40 L0 40Z" fill="var(--navy)"/><path d="M0 27 C150 25 330 14 502 0 L502 4 C330 18 150 28 0 30Z" fill="var(--orange)"/><path d="M220 40 C330 34 420 24 502 12 L502 40Z" fill="#fff"/></svg>
  <div class="url">www.meridalecrestadvisors.example</div>
  <div class="brand">Meridale Crest Advisors</div>
</section>

<!-- Row 8 -->
<section class="slide col-l" style="top:2269px">
  <h2 class="h abs center" style="left:0;width:502px;top:20px;font-size:13.5px">Engagement <span class="o">Options</span></h2>
  <svg class="abs" style="left:176px;top:56px" width="140" height="140" viewBox="0 0 140 140">
    <circle cx="70" cy="70" r="46" fill="none" stroke="var(--navy)" stroke-width="30" stroke-dasharray="51.8 6" transform="rotate(-118 70 70)"/>
    <g fill="var(--orange)" stroke="#fff" stroke-width="2"><circle cx="24" cy="30" r="9"/><circle cx="94" cy="27" r="9"/><circle cx="118" cy="93" r="9"/><circle cx="70" cy="130" r="9"/><circle cx="22" cy="95" r="9"/></g>
    <g style="color:var(--navy)" fill="var(--navy)">
      <use href="#i-gear" x="18" y="24" width="12" height="12"/>
      <use href="#i-chart" x="88" y="21" width="12" height="12"/>
      <use href="#i-up" x="112" y="87" width="12" height="12"/>
      <use href="#i-target" x="64" y="124" width="12" height="12"/>
      <use href="#i-network" x="16" y="89" width="12" height="12"/>
    </g>
  </svg>
  <p class="eng" style="left:100px;top:60px;text-align:right">Franchise Sales<br>Outsourcing</p>
  <p class="eng" style="left:318px;top:60px">Franchise Growth<br>Consulting</p>
  <p class="eng" style="left:78px;top:152px;text-align:right">Broker Network<br>Development</p>
  <p class="eng" style="left:338px;top:152px">Franchise<br>Expansion Strategy</p>
  <p class="eng center" style="left:0;width:502px;top:225px">Franchise Development Advisory Services</p>
  <svg class="footer" viewBox="0 0 502 40"><path d="M0 30 C150 28 330 18 502 4 L502 40 L0 40Z" fill="var(--navy)"/><path d="M0 27 C150 25 330 14 502 0 L502 4 C330 18 150 28 0 30Z" fill="var(--orange)"/><path d="M220 40 C330 34 420 24 502 12 L502 40Z" fill="#fff"/></svg>
  <div class="url">www.meridalecrestadvisors.example</div>
  <div class="brand">Meridale Crest Advisors</div>
</section>

<section class="slide col-r" style="top:2269px;background:var(--navy-deep)">
  <div class="photo" role="img" aria-label="Photo of a smiling senior executive in a suit" style="left:200px;top:0;width:302px;height:230px;background:linear-gradient(90deg,var(--navy-deep) 0%,#4a4f58 40%,#8a8f96 70%,#3b3f46 100%)"></div>
  <h2 class="h abs" style="left:38px;top:34px;font-size:14.5px;color:#fff">Let's Build<br>Your Growth Plan</h2>
  <p class="h abs o" style="left:38px;top:78px;font-size:12px">Schedule a Franchise<br>Growth Strategy Consultation</p>
  <div class="abs" style="left:38px;top:128px;font-size:7.5px;font-weight:700;color:#fff;line-height:20px">
    <div style="display:flex;align-items:center;gap:6px"><svg width="12" height="12" viewBox="0 0 12 12"><circle cx="6" cy="6" r="5.5" fill="none" stroke="var(--orange)"/><path d="M6 3 a2 2 0 0 1 2 2 c0 1.5-2 4-2 4 s-2-2.5-2-4 a2 2 0 0 1 2-2z" fill="var(--orange)"/></svg>+123456789</div>
    <div style="display:flex;align-items:center;gap:6px"><svg width="12" height="12" viewBox="0 0 12 12"><circle cx="6" cy="6" r="5.5" fill="none" stroke="var(--orange)"/><rect x="3" y="4" width="6" height="4" fill="none" stroke="var(--orange)" stroke-width=".8"/><path d="M3 4 L6 6.3 L9 4" fill="none" stroke="var(--orange)" stroke-width=".8"/></svg>info@meridalecrestadvisors.example</div>
    <div style="display:flex;align-items:center;gap:6px"><svg width="12" height="12" viewBox="0 0 12 12"><circle cx="6" cy="6" r="5.5" fill="none" stroke="var(--orange)"/><circle cx="6" cy="6" r="3" fill="none" stroke="var(--orange)" stroke-width=".8"/><path d="M3 6 H9 M6 3 V9" stroke="var(--orange)" stroke-width=".8"/></svg>www.meridalecrestadvisors.example</div>
  </div>
  <svg class="abs" style="left:0;bottom:0" width="502" height="110" viewBox="0 0 502 110"><path d="M0 60 C150 62 330 40 502 0 L502 110 L0 110Z" fill="var(--navy)"/><path d="M0 62 C170 64 340 52 502 22 L502 110 L0 110Z" fill="#fff"/><path d="M0 66 C140 68 300 62 430 50 C300 78 160 92 0 110Z" fill="var(--orange)"/></svg>
  <div class="brand" style="bottom:28px;font-size:10px">Meridale Crest Advisors</div>
</section>

</body>
</html>
```